Business Card Design Project

commercial exhaust hood cleaning and kitchen cleaning

Industry/Entity Type

Business

Contact Information for Business Card

a logo and name on front

```html
<!DOCTYPE html>
<html lang="en">
<head>
<meta charset="UTF-8">
<title>Business Card – Commercial Exhaust Hood Cleaning</title>
<link href="https://fonts.googleapis.com/css2?family=Raleway:wght@400;600;700&display=swap" rel="stylesheet">
<style>
  :root {
    --backdrop: #bcbdbf;
    --card: #ffffff;
    --ink: #58585a;
    --slate: #8c94a0;
    --sage: #8aa59f;
    --charcoal: #58585a;
    --band-text: #ffffff;
  }
  html, body {
    margin: 0;
    padding: 0;
    width: 1200px;
    height: 1000px;
    overflow: hidden;
    background: var(--backdrop);
    font-family: "Raleway", sans-serif;
  }
  .business-card {
    position: absolute;
    left: 265px;
    top: 309px;
    width: 670px;
    height: 382px;
    border-radius: 28px;
    overflow: hidden;
    background: var(--card);
    color: var(--ink);
  }
  .card-shapes {
    position: absolute;
    inset: 0;
  }
  .brand-name {
    position: absolute;
    left: 48px;
    top: 50px;
    margin: 0;
    font-size: 44px;
    font-weight: 600;
    letter-spacing: -0.3px;
    line-height: 1;
  }
  .service-band {
    position: absolute;
    left: 0;
    top: 151px;
    width: 100%;
    height: 40px;
    background: var(--charcoal);
    color: var(--band-text);
    font-size: 20.5px;
    font-weight: 600;
    line-height: 40px;
    padding-left: 35px;
    box-sizing: border-box;
    margin: 0;
  }
  .contact-block {
    position: absolute;
    left: 173px;
    top: 203px;
  }
  .person-name {
    margin: 0;
    font-size: 28px;
    font-weight: 700;
    line-height: 34px;
  }
  .person-role {
    margin: 0 0 20px;
    font-size: 17px;
    font-weight: 400;
    line-height: 20px;
  }
  .contact-list {
    list-style: none;
    margin: 0;
    padding: 0;
    font-size: 17px;
    font-weight: 400;
    line-height: 22.5px;
  }
</style>
</head>
<body>
  <div class="business-card">
    <svg class="card-shapes" width="670" height="382" viewBox="0 0 670 382" aria-hidden="true">
      <circle class="corner-top-right" cx="714" cy="-96" r="223" fill="var(--slate)"/>
      <circle class="corner-bottom-right" cx="704" cy="439" r="205" fill="var(--sage)"/>
      <circle class="corner-bottom-left" cx="-21" cy="407" r="138" fill="var(--charcoal)"/>
    </svg>

    <h1 class="brand-name">Your Logo</h1>

    <p class="service-band">commercial exhaust hood cleaning and kitchen cleaning</p>

    <div class="contact-block">
      <h2 class="person-name">Your Name</h2>
      <p class="person-role">Founder, CEO</p>
      <ul class="contact-list">
        <li>0123-456-123</li>
        <li>name@yourdomain.com</li>
        <li>www.yourdomain.com</li>
      </ul>
    </div>
  </div>
</body>
</html>
```